Slide Master for Halvern Engines - A Systematic Hedge Fund

We are looking for someone to produce a theme and slide master for us for our investor presentations. I have uploaded a few examples of templates that we would like to have included:
Main Title
Section Title
Slides with just bullet points
Different image/table configurations with bullet points and foot notes
Biographies of different lengths
A disclaimer (no one will read this but it should still look nice and needs to be in the presentations)
I have also uploaded the company logo, business card and colour definitions. Currently we have a blue colour scheme defined, but it would be nice to get a complementary set of colours so that when we have charts with more elements we can just draw from those.
The most important thing is that the slide master must be of general use to us. We arn't looking to have a specific presentation designed for us, but a theme/style that we can apply ourselves to any presentation we need to give in the future. It should have clearly defined guidelines for where content should go (and if this is different with and without footnotes for example). We would also like it to have a similar feel to the logo/business cards, so matt colours, high contrast, but not busy.
I'm excited to see the results!

```html
<!DOCTYPE html>
<html lang="en">
<head>
<meta charset="utf-8">
<title>Halvern Engines – Slide Master</title>
<link rel="stylesheet" href="https://fonts.googleapis.com/css2?family=Montserrat:wght@300;400;500;600;700;800&family=Roboto:wght@400;500&display=swap">
<style>
:root{
  --canvas:#e1e1e3;
  --navy:#0c3d72;
  --navy-deep:#082c55;
  --blue:#1f5fa8;
  --sky:#4a8fd6;
  --sky-soft:#c8dcf2;
  --sky-pale:#e7f0fa;
  --ink:#222831;
  --ink-soft:#5b6470;
  --white:#ffffff;
  --charcoal:#1c1c1e;
}
*{margin:0;padding:0;box-sizing:border-box}
html,body{width:1200px;height:3363px;overflow:hidden;background:var(--canvas)}
body{position:relative;font-family:"Montserrat",sans-serif;color:var(--ink)}

.slide{position:absolute;width:540px;height:304px;overflow:hidden;background:var(--white)}
.hero-wrap{position:absolute;left:189px;top:107px;width:823px;height:463px;overflow:hidden}
.hero-wrap .slide{left:0;top:0;transform:scale(1.524);transform-origin:0 0}

/* brand wordmark */
.brand{position:absolute;font-family:"Montserrat",sans-serif;font-weight:700;color:var(--navy);text-transform:uppercase;letter-spacing:.06em;line-height:1.05}
.title-slide .brand{left:40px;top:52px;font-size:11px}
.brand-small{right:22px;top:20px;font-size:6px;text-align:right}
.on-dark .brand{color:var(--white)}

/* title slides */
.title-slide .title{position:absolute;left:39px;top:112px;font-weight:800;font-size:23.5px;line-height:32px;color:var(--navy);white-space:nowrap}
.title-slide .subtitle{position:absolute;left:39px;top:183px;font-weight:400;font-size:13.5px;line-height:16.5px;color:var(--sky)}
.title-slide .date{position:absolute;left:39px;top:241px;font-size:5.5px;color:var(--ink)}
.title-slide .art{position:absolute;left:290px;top:40px;width:230px;height:215px;border-radius:50%}
.art-laptop{background:radial-gradient(circle at 55% 55%,#5d6a78 0 22%,#3ec7d8 23% 34%,#d5dcec 35% 62%,rgba(232,236,246,0) 63%)}
.art-bulbs{background:radial-gradient(circle at 55% 50%,#f2c58a 0 18%,#b9b5e6 19% 45%,#e2e0f4 46% 62%,rgba(240,240,250,0) 63%)}
.on-dark .title,.on-dark .subtitle,.on-dark .date{color:var(--white)}
.theme-blue{background:linear-gradient(90deg,#0f3f75 0%,#2f6cb3 50%,#5d9ce3 100%)}
.theme-dark{background:linear-gradient(90deg,#1b1b1d 0%,#2a2a2c 55%,#3e3e40 100%)}
.title-band{position:absolute;left:0;right:0;bottom:0;height:13px;background:var(--navy);color:var(--white);font-size:4.3px;text-align:center;line-height:13px}
.on-dark .title-band{background:rgba(0,0,0,.22)}
.title-band b,.slide-foot b{font-weight:700}

/* content slides */
.slide-head{position:absolute;left:25px;top:20px}
.slide-head h2{font-family:"Roboto",sans-serif;font-weight:500;font-size:17px;color:var(--ink);line-height:20px}
.slide-head p{font-size:5.5px;color:var(--ink-soft);margin-top:1px}
.slide-head::after{content:"";display:block;width:10px;height:1.5px;background:var(--sky);margin-top:4px}
.slide-foot{position:absolute;left:0;right:0;bottom:0;height:15px}
.slide-foot .foot-text{position:absolute;left:13px;right:13px;top:2px;display:flex;justify-content:space-between;font-size:4.2px;color:var(--ink)}
.slide-foot .page{padding-left:5px;margin-left:4px;border-left:.6px solid var(--ink)}
.slide-foot::after{content:"";position:absolute;left:0;right:0;bottom:0;height:6px;background:var(--navy)}

.fine{font-size:4.7px;line-height:6.1px;color:var(--ink);text-align:justify}
.fine + .fine{margin-top:6px}
.bullets{list-style:none;font-size:6.4px;line-height:8.6px;color:var(--ink)}
.bullets li{position:relative;padding-left:8px;margin-bottom:3px}
.bullets li::before{content:"";position:absolute;left:1px;top:3.2px;width:2px;height:2px;border-radius:50%;background:var(--sky)}
.bullets.light{color:var(--white)}
.bullets.light li::before{background:var(--white)}

.footnote{position:absolute;left:25px;right:13px;height:9px;background:var(--sky-soft);font-size:4.1px;line-height:9px;color:var(--ink);padding-left:8px;white-space:nowrap;overflow:hidden}
.footnote::before{content:"";position:absolute;left:3px;top:1.5px;width:.8px;height:6px;background:var(--navy)}

/* disclaimer */
.disclaimer-cols{position:absolute;left:25px;right:25px;top:86px;display:grid;grid-template-columns:repeat(3,1fr);gap:20px}

/* section and contact */
.photo-bg{position:absolute;inset:0}
.section-photo{background:linear-gradient(120deg,#1e4f8c 0%,#3b6fb0 45%,#7aa3d4 100%)}
.contact-photo{background:linear-gradient(120deg,#0f3a6e 0%,#1d5596 55%,#5e8dc4 100%)}
.section-break .brand,.contact .brand{left:56px;font-size:10px;color:var(--white)}
.section-break .brand{top:122px}
.section-break h2{position:absolute;left:56px;top:163px;font-size:29px;font-weight:700;color:var(--white);line-height:34px}
.section-break h2 span{font-weight:300}
.section-break p{position:absolute;left:56px;top:206px;width:240px;font-size:9.3px;line-height:11px;color:var(--white)}
.contact .brand{top:118px}
.contact h2{position:absolute;left:56px;top:175px;font-size:11px;font-weight:700;color:var(--white)}
.contact-list{position:absolute;left:56px;top:200px;list-style:none;color:var(--white);font-size:6.4px}
.contact-list li{display:flex;align-items:center;gap:6px;height:15px}
.contact-list svg{width:8px;height:8px}
.contact .copy{position:absolute;right:60px;bottom:10px;font-size:4px;color:var(--white)}

/* two boxes */
.box{position:absolute;top:123px;width:230px}
.box h3{height:18px;line-height:18px;padding-left:14px;background:var(--sky);color:var(--white);font-size:8px;font-weight:700;border-radius:0 10px 10px 0}
.box .bullets{margin-top:8px;padding-left:14px;font-size:6.2px}

/* chart slide */
.bullet-band{position:absolute;left:0;right:0;top:80px;height:37px;background:var(--sky);display:grid;grid-template-columns:1fr 1fr;gap:20px;padding:5px 30px 0 30px}
.bullet-band .bullets{font-size:5.3px;line-height:6.4px}
.bullet-band .bullets li{margin-bottom:1px}
.chart{position:absolute;top:124px;width:245px;height:136px}

/* image + bullets */
.photo-box{position:absolute;left:277px;top:102px;width:235px;height:128px;background:linear-gradient(135deg,#1d3e66 0%,#5f86b4 55%,#d2dde9 100%)}

/* table */
.table-title{position:absolute;left:31px;top:88px;font-size:8.5px;font-weight:700;color:var(--navy)}
.table-title span{font-weight:400;color:var(--sky)}
.data-table{position:absolute;left:29px;top:104px;width:343px;border-collapse:collapse;font-size:5px}
.data-table th{background:var(--navy);color:var(--white);font-weight:500;text-align:left;padding:0 3px;height:10px;border-right:.6px solid var(--white)}
.data-table td{height:26px;border-right:.5px solid #e4e8ee;border-bottom:.5px solid #e4e8ee}
.side-box{position:absolute;left:384px;top:102px;width:143px;height:134px;background:var(--navy);padding:12px 10px 0 10px}
.side-box .bullets{font-size:6.2px;line-height:7.4px}

/* text + chart */
.text-block{position:absolute;left:31px;width:225px}
.text-block h3,.bio h3{font-size:9px;font-weight:700;color:var(--navy);margin-bottom:4px}
.text-block h3 span,.bio h3 span{font-weight:400;color:var(--sky)}
.text-block p{font-size:5.8px;line-height:7px}

/* bios */
.bio{position:absolute}
.bio h3{font-size:8.5px}
</style>
</head>
<body>

<!-- Hero: main title slide -->
<div class="hero-wrap">
  <section class="slide title-slide">
    <div class="brand">Halvern<br>Engines</div>
    <h1 class="title">Presentations<br>Title Goes Here!</h1>
    <p class="subtitle">Subtitle of Presentation<br>Goes Here!</p>
    <p class="date">Saturday, June 5, 2021</p>
    <div class="art art-laptop" role="img" aria-label="Illustration of a laptop surrounded by floating dashboard screens and charts"></div>
    <div class="title-band">© 2021 <b>Halvern Engines.</b> All rights reserved.</div>
  </section>
</div>

<!-- Row 1 -->
<section class="slide title-slide" style="left:51px;top:751px">
  <div class="brand">Halvern<br>Engines</div>
  <h1 class="title">Presentations<br>Title Goes Here!</h1>
  <p class="subtitle">Subtitle of Presentation<br>Goes Here!</p>
  <p class="date">Saturday, June 5, 2021</p>
  <div class="art art-laptop" role="img" aria-label="Illustration of a laptop with floating dashboard screens"></div>
  <div class="title-band">© 2021 <b>Halvern Engines.</b> All rights reserved.</div>
</section>
<section class="slide title-slide" style="left:610px;top:751px">
  <div class="brand">Halvern<br>Engines</div>
  <h1 class="title">Presentations<br>Title Goes Here!</h1>
  <p class="subtitle">Subtitle of Presentation<br>Goes Here!</p>
  <p class="date">Saturday, June 5, 2021</p>
  <div class="art art-bulbs" role="img" aria-label="Illustration of two light bulbs on gears with small figures"></div>
  <div class="title-band">© 2021 <b>Halvern Engines.</b> All rights reserved.</div>
</section>

<!-- Row 2 -->
<section class="slide title-slide on-dark theme-blue" style="left:51px;top:1073px">
  <div class="brand">Halvern<br>Engines</div>
  <h1 class="title">Presentations<br>Title Goes Here!</h1>
  <p class="subtitle">Subtitle of Presentation<br>Goes Here!</p>
  <p class="date">Saturday, June 5, 2021</p>
  <div class="art art-laptop" role="img" aria-label="Illustration of a laptop with floating dashboard screens"></div>
  <div class="title-band">© 2021 <b>Halvern Engines.</b> All rights reserved.</div>
</section>
<section class="slide title-slide on-dark theme-blue" style="left:610px;top:1073px">
  <div class="brand">Halvern<br>Engines</div>
  <h1 class="title">Presentations<br>Title Goes Here!</h1>
  <p class="subtitle">Subtitle of Presentation<br>Goes Here!</p>
  <p class="date">Saturday, June 5, 2021</p>
  <div class="art art-bulbs" role="img" aria-label="Illustration of two light bulbs on gears with small figures"></div>
  <div class="title-band">© 2021 <b>Halvern Engines.</b> All rights reserved.</div>
</section>

<!-- Row 3 -->
<section class="slide title-slide on-dark theme-dark" style="left:51px;top:1395px">
  <div class="brand">Halvern<br>Engines</div>
  <h1 class="title">Presentations<br>Title Goes Here!</h1>
  <p class="subtitle">Subtitle of Presentation<br>Goes Here!</p>
  <p class="date">Saturday, June 5, 2021</p>
  <div class="art art-laptop" role="img" aria-label="Illustration of a laptop with floating dashboard screens"></div>
  <div class="title-band">© 2021 <b>Halvern Engines.</b> All rights reserved.</div>
</section>
<section class="slide title-slide on-dark theme-dark" style="left:610px;top:1395px">
  <div class="brand">Halvern<br>Engines</div>
  <h1 class="title">Presentations<br>Title Goes Here!</h1>
  <p class="subtitle">Subtitle of Presentation<br>Goes Here!</p>
  <p class="date">Saturday, June 5, 2021</p>
  <div class="art art-bulbs" role="img" aria-label="Illustration of two light bulbs on gears with small figures"></div>
  <div class="title-band">© 2021 <b>Halvern Engines.</b> All rights reserved.</div>
</section>

<!-- Row 4 -->
<section class="slide disclaimer" style="left:51px;top:1717px">
  <div class="slide-head"><h2>Disclaimer</h2></div>
  <div class="brand brand-small">Halvern<br>Engines</div>
  <div class="disclaimer-cols">
    <div>
      <p class="fine">Lorem ipsum dolor sit amet, consectetur adipiscing elit. Vestibulum lacinia eros eu pharetra mollis. Nullam vulputate purus mi, sed maximus est sodales mollis. Mauris nec vulputate eros. Cras lectus lacus, lacinia eu dapibus ac, tincidunt eu nisi. Suspendisse in volutpat risus. Nunc pharetra porttitor lorem. Proin est odio, suscipit vitae magna at, bibendum tincidunt mi. Aenean facilisis pharetra lacus sed tempus. Nam finibus eu diam eu consectetur. Donec blandit nulla ac erat condimentum, fringilla feugiat ex porttitor.</p>
      <p class="fine">Lorem ipsum dolor sit amet, consectetur adipiscing elit. Vestibulum lacinia eros eu pharetra mollis. Nullam vulputate purus mi, sed maximus est sodales mollis. Mauris nec vulputate eros. Cras lectus lacus, lacinia eu dapibus ac, tincidunt eu nisi. Suspendisse in volutpat risus.</p>
    </div>
    <div>
      <p class="fine">Lorem ipsum dolor sit amet, consectetur adipiscing elit. Vestibulum lacinia eros eu pharetra mollis. Nullam vulputate purus mi, sed maximus est sodales mollis. Mauris nec vulputate eros. Cras lectus lacus, lacinia eu dapibus ac, tincidunt eu nisi. Suspendisse in volutpat risus. Nunc pharetra porttitor lorem. Proin est odio, suscipit vitae magna at, bibendum tincidunt mi. Aenean facilisis pharetra lacus sed tempus. Nam finibus eu diam eu consectetur. Donec blandit nulla ac erat condimentum, fringilla feugiat ex porttitor.</p>
      <p class="fine">Lorem ipsum dolor sit amet, consectetur adipiscing elit. Vestibulum lacinia eros eu pharetra mollis. Nullam vulputate purus mi, sed maximus est sodales mollis. Mauris nec vulputate eros. Cras lectus lacus, lacinia eu dapibus ac, tincidunt eu nisi. Suspendisse in volutpat risus.</p>
    </div>
    <div>
      <p class="fine">Lorem ipsum dolor sit amet, consectetur adipiscing elit. Vestibulum lacinia eros eu pharetra mollis. Nullam vulputate purus mi, sed maximus est sodales mollis. Mauris nec vulputate eros. Cras lectus lacus, lacinia eu dapibus ac, tincidunt eu nisi. Suspendisse in volutpat risus.</p>
      <p class="fine">Lorem ipsum dolor sit amet, consectetur adipiscing elit. Vestibulum lacinia eros eu pharetra mollis. Nullam vulputate purus mi, sed maximus est sodales mollis. Mauris nec vulputate eros. Nunc pharetra porttitor lorem. Proin est odio, suscipit vitae magna at, bibendum tincidunt mi. Aenean facilisis pharetra lacus sed tempus. Nam finibus eu diam eu consectetur. Donec blandit nulla ac erat condimentum, fringilla feugiat ex porttitor.</p>
    </div>
  </div>
  <div class="slide-foot"><div class="foot-text"><span>© 2021 <b>Halvern Engines.</b> All rights reserved.</span><span>Not For Circulation<span class="page">7</span></span></div></div>
</section>

<section class="slide section-break" style="left:610px;top:1717px">
  <div class="photo-bg section-photo" role="img" aria-label="Blue-toned photo of colleagues reviewing documents and a tablet at a desk"></div>
  <div class="brand">Halvern<br>Engines</div>
  <h2>Section <span>Break</span></h2>
  <p>Lorem ipsum dolor sit amet, consectetur adipiscing elit. Vestibulum lacinia eros eu pharetra mollis. Nullam vulputate purus.</p>
</section>

<!-- Row 5 -->
<section class="slide" style="left:51px;top:2039px">
  <div class="slide-head"><h2>Slide Title Goes Here!</h2><p>Subtitle of Slide Goes Here!</p></div>
  <div class="brand brand-small">Halvern<br>Engines</div>
  <div class="box" style="left:30px">
    <h3>Title Goes Here!</h3>
    <ul class="bullets">
      <li>Lorem ipsum dolor sit amet.</li>
      <li>Vestibulum lacinia eros eu pharetra mollis.</li>
      <li>Nullam vulputate purus mi.</li>
      <li>Mauris nec vulputate eros.</li>
      <li>Vestibulum lacinia eros eu pharetra mollis.</li>
    </ul>
  </div>
  <div class="box" style="left:280px">
    <h3>Title Goes Here!</h3>
    <ul class="bullets">
      <li>Lorem ipsum dolor sit amet.</li>
      <li>Vestibulum lacinia eros eu pharetra mollis.</li>
      <li>Nullam vulputate purus mi.</li>
      <li>Mauris nec vulputate eros.</li>
      <li>Vestibulum lacinia eros eu pharetra mollis.</li>
    </ul>
  </div>
  <div class="slide-foot"><div class="foot-text"><span>© 2021 <b>Halvern Engines.</b> All rights reserved.</span><span>Not For Circulation<span class="page">9</span></span></div></div>
</section>

<section class="slide" style="left:610px;top:2039px">
  <div class="slide-head"><h2>Slide Title Goes Here!</h2><p>Subtitle of Slide Goes Here!</p></div>
  <div class="brand brand-small">Halvern<br>Engines</div>
  <div class="bullet-band">
    <ul class="bullets light">
      <li>Lorem ipsum dolor sit amet, consectetur adipiscing elit.</li>
      <li>Lorem ipsum dolor sit amet, consectetur adipiscing elit. Vestibulum lacinia eros eu pharetra mollis.</li>
    </ul>
    <ul class="bullets light">
      <li>Mauris nec vulputate eros. Cras lectus lacus, lacinia eu dapibus ac, tincidunt eu nisi.</li>
      <li>Lorem ipsum dolor sit amet, consectetur adipiscing elit.</li>
    </ul>
  </div>
  <svg class="chart" style="left:15px" viewBox="0 0 245 136">
    <text x="122" y="8" font-size="5" fill="#5b6470" text-anchor="middle" font-family="Montserrat, sans-serif">Chart Title</text>
    <g font-size="4.5" fill="#5b6470" font-family="Montserrat, sans-serif" text-anchor="end">
      <text x="14" y="19">6</text><text x="14" y="34">5</text><text x="14" y="49">4</text><text x="14" y="64">3</text><text x="14" y="79">2</text><text x="14" y="94">1</text><text x="14" y="109">0</text>
    </g>
    <line x1="20" y1="108" x2="240" y2="108" stroke="#d5dae2" stroke-width=".6"/>
    <g>
      <rect x="34" y="43.5" width="8" height="64.5" fill="#0c3d72"/><rect x="43" y="72" width="8" height="36" fill="#4a8fd6"/><rect x="52" y="78" width="8" height="30" fill="#a9c8ec"/>
      <rect x="89" y="70.5" width="8" height="37.5" fill="#0c3d72"/><rect x="98" y="42" width="8" height="66" fill="#4a8fd6"/><rect x="107" y="78" width="8" height="30" fill="#a9c8ec"/>
      <rect x="144" y="55.5" width="8" height="52.5" fill="#0c3d72"/><rect x="153" y="81" width="8" height="27" fill="#4a8fd6"/><rect x="162" y="63" width="8" height="45" fill="#a9c8ec"/>
      <rect x="199" y="40.5" width="8" height="67.5" fill="#0c3d72"/><rect x="208" y="66" width="8" height="42" fill="#4a8fd6"/><rect x="217" y="33" width="8" height="75" fill="#a9c8ec"/>
    </g>
    <g font-size="4.5" fill="#5b6470" font-family="Montserrat, sans-serif" text-anchor="middle">
      <text x="47" y="116">Category 1</text><text x="102" y="116">Category 2</text><text x="157" y="116">Category 3</text><text x="212" y="116">Category 4</text>
    </g>
  </svg>
  <svg class="chart" style="left:270px" viewBox="0 0 245 136">
    <text x="122" y="8" font-size="5" fill="#5b6470" text-anchor="middle" font-family="Montserrat, sans-serif">Chart Title</text>
    <g font-size="4.5" fill="#5b6470" font-family="Montserrat, sans-serif" text-anchor="end">
      <text x="14" y="19">6</text><text x="14" y="34">5</text><text x="14" y="49">4</text><text x="14" y="64">3</text><text x="14" y="79">2</text><text x="14" y="94">1</text><text x="14" y="109">0</text>
    </g>
    <line x1="20" y1="108" x2="240" y2="108" stroke="#d5dae2" stroke-width=".6"/>
    <g>
      <rect x="34" y="43.5" width="8" height="64.5" fill="#0c3d72"/><rect x="43" y="72" width="8" height="36" fill="#4a8fd6"/><rect x="52" y="78" width="8" height="30" fill="#a9c8ec"/>
      <rect x="89" y="70.5" width="8" height="37.5" fill="#0c3d72"/><rect x="98" y="42" width="8" height="66" fill="#4a8fd6"/><rect x="107" y="78" width="8" height="30" fill="#a9c8ec"/>
      <rect x="144" y="55.5" width="8" height="52.5" fill="#0c3d72"/><rect x="153" y="81" width="8" height="27" fill="#4a8fd6"/><rect x="162" y="63" width="8" height="45" fill="#a9c8ec"/>
      <rect x="199" y="40.5" width="8" height="67.5" fill="#0c3d72"/><rect x="208" y="66" width="8" height="42" fill="#4a8fd6"/><rect x="217" y="33" width="8" height="75" fill="#a9c8ec"/>
    </g>
    <g font-size="4.5" fill="#5b6470" font-family="Montserrat, sans-serif" text-anchor="middle">
      <text x="47" y="116">Category 1</text><text x="102" y="116">Category 2</text><text x="157" y="116">Category 3</text><text x="212" y="116">Category 4</text>
    </g>
  </svg>
  <div class="footnote" style="top:263px">Footnote Goes Here! Lorem ipsum dolor sit amet, consectetur adipiscing elit. Vestibulum lacinia eros eu pharetra mollis. Nullam vulputate purus mi, sed maximus.</div>
  <div class="slide-foot"><div class="foot-text"><span>© 2021 <b>Halvern Engines.</b> All rights reserved.</span><span>Not For Circulation<span class="page">10</span></span></div></div>
</section>

<!-- Row 6 -->
<section class="slide" style="left:51px;top:2360px">
  <div class="slide-head"><h2>Slide Title Goes Here!</h2><p>Subtitle of Slide Goes Here!</p></div>
  <div class="brand brand-small">Halvern<br>Engines</div>
  <ul class="bullets" style="position:absolute;left:38px;top:104px;width:222px;font-size:7px;line-height:7.8px">
    <li>Lorem ipsum dolor sit amet, consectetur adipiscing elit. Vestibulum lacinia eros eu pharetra mollis.</li>
    <li>Nullam vulputate purus mi, sed maximus est sodales mollis. Mauris nec vulputate eros.</li>
    <li>Cras lectus lacus, lacinia eu dapibus ac, tincidunt eu nisi. Suspendisse in volutpat risus.</li>
    <li>Nunc pharetra porttitor lorem. Vivamus at lectus sit amet lacus dictum tincidunt at vel magna.</li>
  </ul>
  <div class="photo-box" role="img" aria-label="Photo of business people pointing at a tablet showing charts"></div>
  <div class="footnote" style="top:256px">Footnote Goes Here! Lorem ipsum dolor sit amet, consectetur adipiscing elit. Vestibulum lacinia eros eu pharetra mollis. Nullam vulputate purus mi, sed.</div>
  <div class="slide-foot"><div class="foot-text"><span>© 2021 <b>Halvern Engines.</b> All rights reserved.</span><span>Footnote Goes Here<span class="page">11</span></span></div></div>
</section>

<section class="slide" style="left:610px;top:2360px">
  <div class="slide-head"><h2>Slide Title Goes Here!</h2><p>Subtitle of Slide Goes Here!</p></div>
  <div class="brand brand-small">Halvern<br>Engines</div>
  <div class="table-title">Table <span>Title Goes Here!</span></div>
  <table class="data-table">
    <thead><tr><th style="width:73px">Title 1</th><th>Title 2</th><th>Title 3</th><th>Title 4</th><th>Title 5</th><th>Title 6</th><th>Title 7</th><th style="width:62px">Title 8</th></tr></thead>
    <tbody>
      <tr><td></td><td></td><td></td><td></td><td></td><td></td><td></td><td></td></tr>
      <tr><td></td><td></td><td></td><td></td><td></td><td></td><td></td><td></td></tr>
      <tr><td></td><td></td><td></td><td></td><td></td><td></td><td></td><td></td></tr>
      <tr><td></td><td></td><td></td><td></td><td></td><td></td><td></td><td></td></tr>
    </tbody>
  </table>
  <div class="side-box">
    <ul class="bullets light">
      <li>Lorem ipsum dolor sit amet, consectetur adipiscing elit.</li>
      <li>Vestibulum lacinia eros eu pharetra mollis. Nullam vulputate purus mi, sed maximus est sodales mollis.</li>
      <li>Mauris nec vulputate eros. Cras lectus lacus, lacinia eu dapibus ac, tincidunt eu nisi.</li>
    </ul>
  </div>
  <div class="footnote" style="top:256px">Footnote Goes Here! Lorem ipsum dolor sit amet, consectetur adipiscing elit. Vestibulum lacinia eros eu pharetra mollis. Nullam vulputate purus mi, sed.</div>
  <div class="slide-foot"><div class="foot-text"><span>© 2021 <b>Halvern Engines.</b> All rights reserved.</span><span>Not For Circulation<span class="page">12</span></span></div></div>
</section>

<!-- Row 7 -->
<section class="slide" style="left:51px;top:2682px">
  <div class="slide-head"><h2>Slide Title Goes Here!</h2><p>Subtitle of Slide Goes Here!</p></div>
  <div class="brand brand-small">Halvern<br>Engines</div>
  <div class="text-block" style="top:97px">
    <h3>Title <span>Goes Here!</span></h3>
    <p>Lorem ipsum dolor sit amet, consectetur adipiscing elit. Vestibulum lacinia eros eu pharetra mollis. Nullam vulputate purus mi, sed maximus est sodales mollis. Mauris nec vulputate eros.</p>
  </div>
  <div class="text-block" style="top:162px">
    <h3>Title <span>Goes Here!</span></h3>
    <p>Lorem ipsum dolor sit amet, consectetur adipiscing elit. Vestibulum lacinia eros eu pharetra mollis. Nullam vulputate purus mi, sed maximus est sodales mollis. Mauris nec vulputate eros.</p>
  </div>
  <svg style="position:absolute;left:276px;top:86px;width:240px;height:150px" viewBox="0 0 240 150">
    <g font-size="4.5" fill="#5b6470" font-family="Montserrat, sans-serif" text-anchor="end">
      <text x="14" y="8">450</text><text x="14" y="21.5">400</text><text x="14" y="35">350</text><text x="14" y="48.5">300</text><text x="14" y="62">250</text><text x="14" y="75.5">200</text><text x="14" y="89">150</text><text x="14" y="102.5">100</text><text x="14" y="116">50</text><text x="14" y="129.5">0</text>
    </g>
    <line x1="20" y1="128" x2="230" y2="128" stroke="#d5dae2" stroke-width=".6"/>
    <g font-size="4.5" fill="#5b6470" font-family="Montserrat, sans-serif" text-anchor="middle">
      <text x="20" y="137">0</text><text x="54" y="137">2</text><text x="88" y="137">4</text><text x="122" y="137">6</text><text x="156" y="137">8</text><text x="190" y="137">10</text><text x="224" y="137">12</text>
    </g>
    <path d="M28 124 C60 118 80 112 100 100 C120 88 125 80 140 60 C150 46 155 16 168 16 C178 16 180 30 188 32 L200 31" fill="none" stroke="#4a8fd6" stroke-width="1.2"/>
    <path d="M28 126 C60 124 90 118 110 104 C130 92 150 86 175 80" fill="none" stroke="#0c3d72" stroke-width="1"/>
  </svg>
  <div class="footnote" style="top:256px">Footnote Goes Here! Lorem ipsum dolor sit amet, consectetur adipiscing elit. Vestibulum lacinia eros eu pharetra mollis. Nullam vulputate purus mi, sed.</div>
  <div class="slide-foot"><div class="foot-text"><span>© 2021 <b>Halvern Engines.</b> All rights reserved.</span><span>Not For Circulation<span class="page">13</span></span></div></div>
</section>

<section class="slide" style="left:610px;top:2682px">
  <div class="slide-head"><h2>Heading For Biographies</h2></div>
  <div class="brand brand-small">Halvern<br>Engines</div>
  <div class="bio" style="left:31px;top:86px;width:228px">
    <h3>Name, <span>Title</span></h3>
    <p class="fine">Lorem ipsum dolor sit amet, consectetur adipiscing elit. Vestibulum lacinia eros eu pharetra mollis. Nullam vulputate purus mi, sed maximus est sodales mollis. Mauris nec vulputate eros. Cras lectus lacus, lacinia eu dapibus ac, tincidunt eu nisi. Suspendisse in volutpat risus. Nunc pharetra porttitor lorem. Proin est odio, suscipit vitae magna at, bibendum tincidunt mi. Aenean facilisis pharetra lacus sed tempus. Nam finibus eu diam eu consectetur. Donec blandit nulla ac erat condimentum, fringilla feugiat ex porttitor.</p>
    <h3 style="margin-top:10px">Another Name, <span>Another Title</span></h3>
    <p class="fine">Lorem ipsum dolor sit amet, consectetur adipiscing elit. Vestibulum lacinia eros eu pharetra mollis. Nullam vulputate purus mi, sed maximus est sodales mollis. Mauris nec vulputate eros. Cras lectus lacus, lacinia eu dapibus ac, tincidunt eu nisi. Suspendisse in volutpat risus.</p>
  </div>
  <div class="bio" style="left:283px;top:100px;width:244px">
    <p class="fine">Lorem ipsum dolor sit amet, consectetur adipiscing elit. Vestibulum lacinia eros eu pharetra mollis. Nullam vulputate purus mi, sed maximus est sodales mollis. Mauris nec vulputate eros. Cras lectus lacus, lacinia eu dapibus ac, tincidunt eu nisi. Suspendisse in volutpat risus. Nunc pharetra porttitor lorem. Proin est odio, suscipit vitae magna at, bibendum tincidunt mi. Aenean facilisis pharetra lacus sed tempus. Nam finibus eu diam eu consectetur. Donec blandit nulla ac erat condimentum, fringilla feugiat ex porttitor.</p>
    <p class="fine">Lorem ipsum dolor sit amet, consectetur adipiscing elit. Vestibulum lacinia eros eu pharetra mollis. Nullam vulputate purus mi, sed maximus est sodales mollis. Mauris nec vulputate eros. Cras lectus lacus, lacinia eu dapibus ac, tincidunt eu nisi. Suspendisse in volutpat risus. Nunc pharetra porttitor lorem. Proin est odio, suscipit vitae magna at, bibendum tincidunt mi. Aenean facilisis pharetra lacus sed tempus. Nam finibus eu diam eu consectetur. Donec blandit nulla ac erat condimentum, fringilla feugiat ex porttitor.</p>
  </div>
  <div class="slide-foot"><div class="foot-text"><span>© 2021 <b>Halvern Engines.</b> All rights reserved.</span><span>Not For Circulation<span class="page">14</span></span></div></div>
</section>

<!-- Row 8 -->
<section class="slide" style="left:51px;top:3004px">
  <div class="slide-head" style="top:28px"><h2>Heading For Biographies</h2></div>
  <div class="brand brand-small">Halvern<br>Engines</div>
  <div class="bio" style="left:31px;top:86px;width:228px">
    <h3>Another Name, <span>Another Title</span></h3>
    <p class="fine">Lorem ipsum dolor sit amet, consectetur adipiscing elit. Vestibulum lacinia eros eu pharetra mollis. Nullam vulputate purus mi, sed maximus est sodales mollis. Mauris nec vulputate eros. Cras lectus lacus, lacinia eu dapibus ac, tincidunt eu nisi. Suspendisse in volutpat risus. Nunc pharetra porttitor lorem. Proin est odio, suscipit vitae magna at, bibendum tincidunt mi. Aenean facilisis pharetra lacus sed tempus. Nam finibus eu diam eu consectetur. Donec blandit nulla ac erat condimentum, fringilla feugiat ex porttitor.</p>
    <p class="fine">Lorem ipsum dolor sit amet, consectetur adipiscing elit. Vestibulum lacinia eros eu pharetra mollis. Nullam vulputate purus mi, sed maximus est sodales mollis. Mauris nec vulputate eros. Cras lectus lacus, lacinia eu dapibus ac, tincidunt eu nisi. Suspendisse in volutpat risus.</p>
  </div>
  <div class="bio" style="left:283px;top:86px;width:228px">
    <h3>Another Name, <span>Another Title</span></h3>
    <p class="fine">Lorem ipsum dolor sit amet, consectetur adipiscing elit. Vestibulum lacinia eros eu pharetra mollis. Nullam vulputate purus mi, sed maximus est sodales mollis. Mauris nec vulputate eros. Cras lectus lacus, lacinia eu dapibus ac, tincidunt eu nisi. Suspendisse in volutpat risus. Nunc pharetra porttitor lorem. Proin est odio, suscipit vitae magna at, bibendum tincidunt mi. Aenean facilisis pharetra lacus sed tempus. Nam finibus eu diam eu consectetur. Donec blandit nulla ac erat condimentum, fringilla feugiat ex porttitor.</p>
    <p class="fine">Lorem ipsum dolor sit amet, consectetur adipiscing elit. Vestibulum lacinia eros eu pharetra mollis. Nullam vulputate purus mi, sed maximus est sodales mollis. Mauris nec vulputate eros. Cras lectus lacus, lacinia eu dapibus ac, tincidunt eu nisi. Suspendisse in volutpat risus.</p>
  </div>
  <div class="slide-foot"><div class="foot-text"><span>© 2021 <b>Halvern Engines.</b> All rights reserved.</span><span>Not For Circulation<span class="page">15</span></span></div></div>
</section>

<section class="slide contact" style="left:610px;top:3004px">
  <div class="photo-bg contact-photo" role="img" aria-label="Blue-toned photo of a business handshake with a faint network pattern"></div>
  <div class="brand">Halvern<br>Engines</div>
  <h2>Contact Us</h2>
  <ul class="contact-list">
    <li><svg viewBox="0 0 10 10"><path d="M2.2 1 L3.8 1 L4.4 3 L3.3 3.9 C3.9 5.2 4.8 6.1 6.1 6.7 L7 5.6 L9 6.2 L9 7.8 C9 8.5 8.5 9 7.8 9 C4.1 8.7 1.3 5.9 1 2.2 C1 1.5 1.5 1 2.2 1 Z" fill="#fff"/></svg>Contact Number Goes Here</li>
    <li><svg viewBox="0 0 10 10"><circle cx="5" cy="5" r="4" fill="none" stroke="#fff" stroke-width="1"/><circle cx="5" cy="5" r="1.6" fill="none" stroke="#fff" stroke-width="1"/></svg>E-Mail Address Goes Here</li>
    <li><svg viewBox="0 0 10 10"><circle cx="5" cy="5" r="4" fill="none" stroke="#fff" stroke-width=".9"/><ellipse cx="5" cy="5" rx="1.8" ry="4" fill="none" stroke="#fff" stroke-width=".8"/><line x1="1" y1="5" x2="9" y2="5" stroke="#fff" stroke-width=".8"/></svg>URL Address Goes Here</li>
  </ul>
  <div class="copy">© 2021 Halvern Engines. All rights reserved.</div>
</section>

</body>
</html>
```